Can you make FairlyNeat look better than average? We need business cards and a logo refresh :-)

REVISED BRIEF

PRIORITY

VECTOR LOGO

Create a vector version of our existing logo. The logo must not change from its current design, weight or font.

Deliverables

- Logo in blue (#2540BB)
- Logo in white (#FFFFFF)
- Logo in grey (#36454F)
- All logos on transparent background
- All logos in PNG & SVG formats. (SVG must NOT distort stroke width when resized)

BRAND MARK

Create a brand mark for use with the logo. This should be possible to used with the logo and on its own as a stand alone graphical device that represents the FAIRLYNEAT brand.

https://quellbrik.com/resources/glossary/what-is-a-brand-mark

Deliverables

- Brand Mark in blue (#2540BB)
- Brand Mark in white (#FFFFFF)
- Brand Mark in grey (#36454F)
- Brand Mark on transparent background
- Brand Mark in PNG & SVG formats. (SVG must NOT distort stroke width when resized)
- Logo combined with Brand Mark (colours and formats)
.

Business Card Layout

Create 2 layouts with the following details:-

Marcus Delaney
Co-Founder & Chief Product Officer

marcus@fairlyneat.nz
www.fairlyneat.nz
0279831465

Callum Ferris
Founder & CEO

hello@fairlyneat.nz
www.fairlyneat.nz
021 684 2590

DESIGN CONSIDERATIONS

Create versions with ‘Shaping Causes With Heart’ tag line incorporated within the design and without (maintain separation of logo from tag line)

- Create a version with and without the brand mark
- Keep it clean and simple but elevate the design with subtle design effects
- Consider use of raised spot gloss colour (this can be white on white for subtle or blue on blue or blue on white)
- Consider use of spot gloss colour (this can be white on white for subtle or blue on blue or blue on white)
- Consider use of letterpress indentation
- Ensure contact details are legible, use sans-serif font

PREVIOUS BRIEF

We need a business card design for our business FairlyNeat. We are a purpose driven brand and media agency that helps brands and charities plan and buy traditional media campaigns (TV, Radio, Print, Outdoor etc). We give a significant amount of the media booking fees we receive from media vendors to charity in the name of our clients. https://www.plinkwork.com/posts/wearefairlyneat_giveback-fairlyneat-shapingcauseswithheart-activity-5829170364418205731-Rtqe

Our strapline is 'Shaping Causes With Heart'.

We want to keep our logo design as it is but it does need tightening up and made into a proper vector image as it's been created from a font.

Our brand colour is #2540BB and we need to keep this.

Our brand is professional but human, warm and engaging and doesn't take itself too seriously.

Things We Need
- vectorisation and tidying up of existing logo
- We'd like you to think about how we can incorporate a brand mark with the logo to add another dimension to our brand
- business card layout and design
- we'll be using zentiprint.com to print the cards so please take a look at the options they have (spot gloss, foil, letterpress, square cards and even the backs of the cards can have a different design on every single card!
- potential opportunity for different famous quotes on the back or imagery or slight design differences
- we'd be open to the use of an emoji or emojiis as the brandmark or to be incorporated into the card designs
- we can have as many different design batches as we like for the backs of the cards

https://www.zentiprint.com/au/business-cards

We want to make an impact, we want to be seen as professional but fun, we want to be different.

Here's a press release of what we're about.

https://adwirely.co.nz/movings-shakings/fairlyneat-welcomes-marcus-delaney-as-co-founder/

Be bold, be different, there is no such thing as a bad idea. We're open to anything so please bring your best ideas and have fun with it! Go crazy if you like!
____________
Marcus Delaney
marcus@fairlyneat.nz
0279831465

Callum Ferris
Founder & CEO
hello@fairlyneat.nz
021 684 2590

Shaping Causes With Heart

________

These are the only details we MUST have on the cards, the rest is up to you. Just make sure you use all of your creativity but don't feel the need to crowd the card with too much, let it breathe as well.

In terms of font for the details, we'll leave that up to you, just ensure it's legible. Oh and please don't take any design inspiration from our website - that will be changing!

Please don't let the design and layout look cheap and tacky though. It needs to still feel premium but personable.

Thanks

Marcus

Many designs are changing the logo and this was NOT in the brief. We need a brand mark to complement the logo. We need to see the logo with and without the brand mark. We need to see the business card with both logo + brand mark and logo on its own We need to see the business card with and without the tagline 'Shaping Causes With Heart'

purpose driven Brand & Media Agency

Shaping Causes With Heart
Marcus Delaney, Co-Founder & Chief Product Officer, marcus@fairlyneat.nz fairlyneet.nz, 0279 831 465

Callum Ferris, Founder & CEO hello@fairlyneat.nz, fairlyneet.nz, 021 684 2590

Serif
Sans Serif

0054AA
0677BA
7BADD7
CADEEF
E8F1F8

• brand mark, vector version of existing logo, Shaping Causes With Heart tagline, existing logo traced and vectorised. Must fully explore the design options from zentiprint.com that can enhance the overall card design
• brandmark to help elevate the logo, maybe incorporate some other design elements into the card like lines, or grids.
• A cheap look and feel

```html
<!DOCTYPE html>
<html lang="en">
<head>
<meta charset="utf-8">
<title>FairlyNeat business cards</title>
<link rel="stylesheet" href="https://fonts.googleapis.com/css2?family=Montserrat:wght@300;400;600;800&display=swap">
<style>
  :root {
    --brand-blue: #2540BB;
    --card-white: #FAFAF8;
    --backdrop: #3A332F;
    --text-blue: #2A44C0;
    --photo-light: #E6E8EE;
    --photo-mid: #4B6FAE;
    --photo-dark: #2F3E5C;
  }
  * { box-sizing: border-box; margin: 0; padding: 0; }
  html, body { width: 1200px; height: 795px; overflow: hidden; }
  body {
    background: var(--backdrop);
    font-family: 'Montserrat', sans-serif;
    position: relative;
  }
  .card {
    position: absolute;
    top: 242px;
    width: 540px;
    height: 310px;
    border-radius: 3px;
    overflow: hidden;
    box-shadow: 0 10px 24px rgba(0,0,0,0.45);
  }
  /* Back of card */
  .card-back {
    left: 30px;
    background: var(--brand-blue);
    color: #FFFFFF;
  }
  .card-back .wordmark {
    position: absolute;
    left: 0; right: 0; top: 108px;
    display: flex; align-items: center; justify-content: center; gap: 12px;
  }
  .card-back .wordmark-square {
    width: 22px; height: 22px; background: #FFFFFF;
  }
  .card-back .wordmark-name {
    font-weight: 600; font-size: 30px; color: #FFFFFF;
  }
  .card-back .tagline {
    position: absolute;
    left: 0; right: 0; top: 178px;
    text-align: center;
    font-weight: 400; font-size: 19px; letter-spacing: 0.3px;
  }
  /* Front of card */
  .card-front {
    left: 630px;
    background: var(--card-white);
    color: var(--text-blue);
  }
  .card-front .wordmark {
    position: absolute; left: 40px; top: 44px;
    display: flex; align-items: center; gap: 10px;
  }
  .card-front .wordmark-square {
    width: 18px; height: 18px; background: var(--brand-blue);
  }
  .card-front .wordmark-name {
    font-weight: 600; font-size: 26px; color: var(--brand-blue);
  }
  .card-front .accent-bar {
    position: absolute; left: 0; top: 106px;
    width: 14px; height: 44px; background: var(--brand-blue);
  }
  .card-front .person-name {
    position: absolute; left: 40px; top: 104px;
    font-weight: 800; font-size: 25px; color: var(--brand-blue);
  }
  .card-front .person-title {
    position: absolute; left: 40px; top: 136px;
    font-weight: 300; font-size: 14px;
  }
  .contact-list {
    position: absolute; left: 40px; top: 176px;
    list-style: none;
    font-weight: 300; font-size: 15px;
  }
  .contact-list li {
    display: flex; align-items: center; gap: 10px;
    height: 26px;
  }
  .contact-icon {
    width: 16px; height: 16px; border-radius: 4px;
    background: var(--brand-blue);
    display: flex; align-items: center; justify-content: center;
    flex: none;
  }
  .portrait {
    position: absolute; right: 18px; bottom: 0;
    width: 190px; height: 205px;
    background: linear-gradient(180deg, var(--photo-light) 0%, var(--photo-mid) 45%, var(--photo-dark) 100%);
    border-radius: 90px 90px 0 0;
  }
</style>
</head>
<body>

  <section class="card card-back" aria-label="Card back">
    <div class="wordmark">
      <span class="wordmark-square"></span>
      <span class="wordmark-name">FairlyNeat</span>
    </div>
    <p class="tagline">Shaping Causes With Heart</p>
  </section>

  <section class="card card-front" aria-label="Card front">
    <div class="wordmark">
      <span class="wordmark-square"></span>
      <span class="wordmark-name">FairlyNeat</span>
    </div>
    <span class="accent-bar"></span>
    <h1 class="person-name">Marcus Delaney</h1>
    <p class="person-title">Co-Founder &amp; Chief Product Officer</p>
    <ul class="contact-list">
      <li>
        <span class="contact-icon">
          <svg width="10" height="10" viewBox="0 0 10 10"><path d="M2 1 L4 1 L4.6 3 L3.4 3.8 Q4.4 5.8 6.2 6.6 L7 5.4 L9 6 L9 8 Q9 9 8 9 Q1 8.6 1 2 Q1 1 2 1 Z" fill="#FFFFFF"/></svg>
        </span>
        0279 831 465
      </li>
      <li>
        <span class="contact-icon">
          <svg width="10" height="10" viewBox="0 0 10 10" fill="none" stroke="#FFFFFF" stroke-width="0.9"><circle cx="5" cy="5" r="4"/><ellipse cx="5" cy="5" rx="1.8" ry="4"/><line x1="1" y1="5" x2="9" y2="5"/></svg>
        </span>
        fairlyneat.nz
      </li>
      <li>
        <span class="contact-icon">
          <svg width="10" height="10" viewBox="0 0 10 10" fill="none" stroke="#FFFFFF" stroke-width="0.9"><rect x="1" y="2.2" width="8" height="5.6"/><polyline points="1,2.2 5,5.6 9,2.2"/></svg>
        </span>
        marcus@fairlyneat.nz
      </li>
    </ul>
    <div class="portrait" role="img" aria-label="Portrait photo of Marcus Delaney in a blue blazer, seated"></div>
  </section>

</body>
</html>
```